Business cards for a new business: Amber Willow Dawn Healing

I would like for the card to include a lotus. The business is a healing practice so I'd like the overall colours to be pink and green and for it to have a soft feel. The name of the practice is
"Amber Willow Dawn Healing", which I'd like to be included, as well as the words: "Energetic and spiritual healing to restore health, harmony and wellbeing". Also, my name - Tovan and the number: 5319 6048

Target Market(s)

Everyone interested in personal healing!

Industry/Entity Type

Business

Contact Information for Business Card

As above……..could be single or double-sided
I'd like the font for the name of the practice and my name to be in green and be a flowing, but simple font - elegant.
The background to be a light pink. See below for colours

Colors
f9d9e8
eea4c8
e567a6
d0ebe7
86cfc6
33b7a4

Requirements
Must have
• See above
Nice to have
• See above

```html
<!DOCTYPE html>
<html lang="en">
<head>
<meta charset="utf-8">
<title>Amber Willow Dawn Healing – Business Card</title>
<link href="https://fonts.googleapis.com/css2?family=Quicksand:wght@500;700&display=swap" rel="stylesheet">
<style>
  :root {
    --page-bg: #f4eef0;
    --card-bg: #f9d9e8;
    --pink-soft: #eea4c8;
    --pink-deep: #e567a6;
    --mint-light: #d0ebe7;
    --mint: #86cfc6;
    --brand-green: #1f9f5c;
    --band-green: #33b7a4;
    --text-dark: #3a2a33;
    --sky-top: #a9c8e8;
    --sky-mid: #e3edf5;
    --grass: #6bb445;
    --grass-deep: #3f8f2a;
  }
  * { margin: 0; padding: 0; box-sizing: border-box; }
  html, body {
    width: 1200px;
    height: 818px;
    overflow: hidden;
    background: var(--page-bg);
    font-family: "Quicksand", "Trebuchet MS", sans-serif;
  }
  .stage {
    width: 1200px;
    height: 818px;
    display: flex;
    align-items: center;
    justify-content: center;
  }
  .card {
    position: relative;
    width: 900px;
    height: 514px;
    background: var(--card-bg);
    border-radius: 4px;
    box-shadow: 0 6px 24px rgba(120, 60, 90, 0.18);
    overflow: hidden;
  }
  .card-art {
    position: absolute;
    inset: 0;
    width: 900px;
    height: 514px;
  }
  .card-content {
    position: absolute;
    left: 390px;
    top: 48px;
    right: 36px;
  }
  .practice-mark {
    display: flex;
    align-items: center;
    gap: 12px;
    color: var(--brand-green);
    font-size: 22px;
    font-weight: 700;
    white-space: nowrap;
  }
  .practice-mark .dot {
    width: 18px;
    height: 18px;
    border-radius: 50%;
    background: var(--pink-deep);
    flex: none;
  }
  .person-name {
    margin-top: 54px;
    color: var(--brand-green);
    font-size: 112px;
    font-weight: 700;
    line-height: 1;
    letter-spacing: -1px;
  }
  .phone {
    margin-top: 6px;
    color: var(--brand-green);
    font-size: 44px;
    font-weight: 500;
    letter-spacing: 1px;
  }
  .tagline {
    margin-top: 44px;
    color: var(--text-dark);
    font-size: 23px;
    font-weight: 500;
    line-height: 1.3;
    white-space: nowrap;
  }
</style>
</head>
<body>
  <main class="stage">
    <article class="card">
      <svg class="card-art" viewBox="0 0 900 514">
        <defs>
          <linearGradient id="meadowGradient" x1="0" y1="0" x2="0" y2="1">
            <stop offset="0" stop-color="#a9c8e8"/>
            <stop offset="0.45" stop-color="#e3edf5"/>
            <stop offset="0.7" stop-color="#6bb445"/>
            <stop offset="1" stop-color="#3f8f2a"/>
          </linearGradient>
        </defs>
        <path class="meadow-photo" role="img"
              aria-label="Photo of a woman stretching her arms in a green meadow under a bright sky"
              d="M0,0 L300,0 Q250,260 345,514 L0,514 Z"
              fill="url(#meadowGradient)"/>
        <path class="curve-band" d="M300,0 Q250,260 345,514"
              fill="none" stroke="#33b7a4" stroke-width="14"/>
      </svg>
      <div class="card-content">
        <div class="practice-mark"><span class="dot"></span>Amber Willow Dawn Healing</div>
        <h1 class="person-name">Tovan</h1>
        <p class="phone">5319 6048</p>
        <p class="tagline">Energetic &amp; Spiritual healing to restore<br>health, harmony and wellbeing</p>
      </div>
    </article>
  </main>
</body>
</html>
```